Design a For Sale sign board and Direction Sign Board.
Attached is an example of what i am thinking but am happy to look at any options.
Colours are to be ""bright Orange"on white and in reverse as well.

Logo id Fairbrook & Co Real Estate.

```html
<!DOCTYPE html>
<html lang="en">
<head>
<meta charset="utf-8">
<title>Fairbrook &amp; Co Real Estate – For Sale Sign</title>
<link rel="stylesheet" href="https://fonts.googleapis.com/css2?family=Rubik:wght@600;700;800&display=swap">
<style>
  :root {
    --backdrop: #b3b3b3;
    --board-white: #f5f5f7;
    --brand-orange: #ffa400;
    --brand-orange-deep: #c17d00;
    --banner-charcoal: #2b2a29;
    --ink: #1c1a1d;
    --pure-white: #ffffff;
  }
  * { margin: 0; padding: 0; box-sizing: border-box; }
  html, body {
    width: 738px;
    height: 1200px;
    overflow: hidden;
    background: var(--backdrop);
    font-family: "Rubik", Arial, sans-serif;
  }
  .canvas {
    position: relative;
    width: 738px;
    height: 1200px;
  }
  .sign-board {
    position: absolute;
    left: 24px;
    top: 141px;
    width: 783px;
    height: 1042px;
    background: var(--board-white);
    transform: scale(0.881);
    transform-origin: 0 0;
    box-shadow: 0 18px 24px -14px rgba(0, 0, 0, 0.35);
  }
  .brand-banner {
    position: absolute;
    left: 0;
    top: 0;
  }
  .brand-name {
    position: absolute;
    left: 34px;
    width: 715px;
    text-align: center;
    color: var(--brand-orange);
    font-weight: 700;
    text-transform: uppercase;
    line-height: 1;
  }
  .brand-name--primary {
    top: 66px;
    font-size: 72px;
    letter-spacing: 0.5px;
  }
  .brand-name--secondary {
    top: 156px;
    font-size: 42px;
    letter-spacing: 2px;
  }
  .headline {
    position: absolute;
    left: 0;
    top: 345px;
    width: 783px;
    text-align: center;
    font-size: 134px;
    font-weight: 800;
    color: var(--ink);
    line-height: 1;
    letter-spacing: 2px;
  }
  .contact-panel {
    position: absolute;
    left: 26px;
    top: 597px;
    width: 731px;
    height: 413px;
    background: var(--brand-orange);
    overflow: hidden;
  }
  .contact-panel__illustration {
    position: absolute;
    left: 16px;
    right: 6px;
    top: 70px;
    bottom: 0;
    background: linear-gradient(180deg, rgba(193, 125, 0, 0.55) 0%, var(--brand-orange-deep) 45%);
    border-radius: 60px 60px 0 0;
  }
  .phone-pill {
    position: absolute;
    left: 46px;
    top: 537px;
    width: 690px;
    height: 110px;
    border: 5px solid var(--pure-white);
    border-radius: 55px;
    background: var(--brand-orange);
    display: flex;
    align-items: center;
    justify-content: center;
    font-size: 86px;
    font-weight: 700;
    color: var(--ink);
    letter-spacing: 3px;
    line-height: 1;
  }
  .agent-name {
    position: absolute;
    left: 0;
    top: 664px;
    width: 783px;
    text-align: center;
    font-size: 48px;
    font-weight: 700;
    color: var(--pure-white);
    letter-spacing: 1px;
    line-height: 1;
  }
</style>
</head>
<body>
  <main class="canvas">
    <section class="sign-board" aria-label="For sale sign">
      <svg class="brand-banner" width="783" height="310" viewBox="0 0 783 310" aria-hidden="true">
        <polygon points="34,35 749,35 749,207 392,297 34,207" fill="var(--brand-orange)"/>
        <polygon points="34,35 749,35 749,187 392,277 34,187" fill="var(--banner-charcoal)"/>
      </svg>
      <p class="brand-name brand-name--primary">Fairbrook &amp; Co</p>
      <p class="brand-name brand-name--secondary">Real Estate</p>

      <h1 class="headline">FOR SALE</h1>

      <div class="contact-panel">
        <div class="contact-panel__illustration" role="img" aria-label="City skyline illustration of tall buildings in deep orange"></div>
      </div>
      <p class="phone-pill">0412-583-027</p>
      <p class="agent-name">ALEX MORGAN</p>
    </section>
  </main>
</body>
</html>
```